Zorpax.com (Dedicated servers Provider)

We provide dedicated servers for clients around the world. We have created a layout for you. You need to create exactly the design based on these sketches. All text, you can take from our sketches (later we will replace them).

Target Market(s)

Web site owners and web developers

Requirements
Should not have
• The design should not use old-style fonts.

```html
<!DOCTYPE html>
<html lang="en">
<head>
<meta charset="utf-8">
<title>Zorpax.com – Dedicated Servers</title>
<link href="https://fonts.googleapis.com/css2?family=Arimo:ital,wght@0,400;0,700;1,400&family=Open+Sans:wght@300;400;600&family=Oswald:wght@500;600&display=swap" rel="stylesheet">
<style>
:root{
  --green:#8cb83a;
  --green-dark:#6f9a24;
  --green-light:#b4d35e;
  --green-text:#7ba42a;
  --dark:#2e2e2c;
  --line:#d6d6d4;
  --soft:#f1f1f0;
  --text:#555553;
  --white:#ffffff;
}
*{box-sizing:border-box;margin:0;padding:0}
html,body{width:1200px;height:2335px;overflow:hidden}
body{position:relative;background:var(--white);font-family:"Arimo",Arial,sans-serif;color:var(--text)}
a{color:inherit}

/* header */
.site-header{position:absolute;left:0;top:0;width:1200px;height:578px;
  background:linear-gradient(180deg,#3c3c3a 0%,#333331 55%,#262624 100%);border-top:4px solid var(--green)}
.top-tab{position:absolute;left:679px;top:-4px;width:432px;height:36px;background:linear-gradient(#9cc547,#7ea82c);
  border-radius:0 0 14px 14px;display:flex;align-items:center;justify-content:center;gap:34px;color:#fff;font-size:18px;white-space:nowrap}
.top-tab span{display:flex;align-items:center;gap:10px}
.brand{position:absolute;left:86px;top:32px;display:flex;align-items:center;gap:14px;color:#fff;font-size:52px;font-weight:700;letter-spacing:1px}
.brand-square{width:48px;height:48px;background:var(--white)}
.account-links{position:absolute;left:548px;top:52px;display:flex}
.account-link{display:flex;gap:10px;width:206px;white-space:nowrap}
.account-link .ico{width:34px;height:34px;border-radius:50%;flex:none}
.account-link:nth-child(1) .ico{background:radial-gradient(circle at 40% 35%,#c9d8ec,#5c79a3)}
.account-link:nth-child(2) .ico{background:radial-gradient(circle at 40% 35%,#d9a56a,#8a5a2e)}
.account-link:nth-child(3) .ico{background:radial-gradient(circle at 40% 35%,#bfe3f7,#3f97c8)}
.account-link b{display:block;font-weight:400;color:var(--green-light);font-size:19px}
.account-link small{display:block;color:#ddd;font-size:14px;text-decoration:underline;margin-top:2px}

.main-nav{position:absolute;left:93px;top:138px;width:1012px;height:47px;display:flex;
  background:linear-gradient(#3a3a38,#1f1f1e);border-radius:4px 4px 0 0}
.main-nav a{display:flex;align-items:center;justify-content:center;color:#e6e6e4;text-decoration:none;font-size:14px;
  border-left:1px solid #4b4b49;white-space:nowrap}
.main-nav a.active{background:linear-gradient(#a5cf4a,#6f9a24);border-left:none;border-radius:4px 0 0 0}

.hero{position:absolute;left:93px;top:189px;width:1012px;height:323px;border-radius:0 0 10px 10px;
  background:linear-gradient(180deg,#6a6a68 0%,#545452 45%,#3a3a38 100%);box-shadow:inset 0 0 0 5px #2a2a28}
.hero-title{position:absolute;left:367px;top:58px;font-family:"Open Sans",sans-serif;font-weight:300;font-size:49px;color:#f2f2f0;white-space:nowrap}
.hero-list{position:absolute;left:54px;top:122px;list-style:none;width:298px}
.hero-list li{height:33px;display:flex;align-items:center;gap:16px;color:#e4e4e2;font-size:16px;white-space:nowrap;
  background:rgba(30,30,28,.35);border-bottom:1px solid rgba(255,255,255,.06);padding-left:10px}
.hero-list svg{flex:none}
.price-box{position:absolute;left:365px;top:132px;width:270px;height:128px;background:rgba(35,35,33,.55);border-radius:4px}
.price-only{position:absolute;left:16px;top:28px;color:#fff;font-size:16px;transform:rotate(-22deg);white-space:nowrap}
.price-link{position:absolute;left:128px;top:10px;color:#f0f0ee;font-size:15px;text-decoration:underline;white-space:nowrap}
.price-value{position:absolute;left:42px;top:38px;font-family:"Oswald",sans-serif;font-weight:600;font-size:76px;line-height:1;color:var(--green-light)}
.price-lock{position:absolute;left:640px;top:133px;width:78px;height:108px;border-radius:10px;background:linear-gradient(#d7d7d5,#8c8c8a)}
.server-rack{position:absolute;left:747px;top:62px;width:265px;height:270px;border-radius:6px;
  background:linear-gradient(90deg,#2a2a2a,#6c6c6c 30%,#222 50%,#5e5e5e 70%,#1d1d1d)}
.dots{position:absolute;left:350px;top:295px;width:140px;height:28px;background:#2a2a28;border-radius:14px 14px 0 0;
  display:flex;align-items:center;justify-content:center;gap:12px}
.dots i{width:11px;height:11px;border-radius:50%;background:#6a6a68}
.dots i:first-child{background:#f4f4f2}

/* info strip */
.info-strip{position:absolute;left:90px;top:578px;width:1020px;height:58px;background:var(--soft);display:flex;align-items:center}
.info-strip p{padding-left:39px;width:815px;font-size:14px;color:#444;white-space:nowrap}
.info-strip p a{color:var(--green-dark);margin-left:12px}
.connect{display:flex;align-items:center;height:100%;padding-left:20px;border-left:1px solid #e0e0de;font-size:13px;font-style:italic;color:#888;white-space:nowrap}
.social-links{position:absolute;left:975px;top:546px;display:flex;gap:16px;font-size:15px;font-weight:700;color:#fff;white-space:nowrap}
.social-links span{display:flex;align-items:center;gap:6px}
.social-links i{width:14px;height:14px;border-radius:50%;background:#4a8fd6}

/* plans */
.plan{position:absolute;top:665px;width:318px;height:251px;border:1px solid #d4d4d2;border-radius:12px;
  background:linear-gradient(#fafaf9,#ececeb);box-shadow:0 6px 10px rgba(0,0,0,.08)}
.plan h3{text-align:center;margin-top:14px;font-weight:400;font-size:28px;color:var(--green-text);letter-spacing:.5px;white-space:nowrap}
.plan .cost{position:absolute;left:38px;top:58px;font-family:"Oswald",sans-serif;font-weight:600;font-size:38px;color:#3c3c3a}
.plan ul{position:absolute;left:170px;top:64px;list-style:none;font-size:14px;color:#444;line-height:26px;white-space:nowrap}
.plan ul li::before{content:"";display:inline-block;width:5px;height:5px;border-radius:50%;background:#444;margin-right:9px;vertical-align:middle}
.plan .art{position:absolute;left:14px;top:118px;width:128px;height:118px;border-radius:10px}
.btn-green{position:absolute;left:170px;top:183px;width:132px;height:32px;border-radius:16px;background:linear-gradient(#b2d65a,#77a22a);
  border:2px solid #d9e9b4;color:#fff;font-size:15px;font-weight:700;display:flex;align-items:center;justify-content:center}

/* features */
.support-photo{position:absolute;left:81px;top:961px;width:305px;height:221px;
  background:linear-gradient(90deg,#f4f4f3 0%,#e9e9e8 30%,#d9d6d2 60%,#efefee 100%)}
.features-intro{position:absolute;left:417px;top:966px;width:660px;font-size:13.5px;line-height:20px;color:#555}
.checks{position:absolute;top:1050px;list-style:none;font-size:18px;color:#333;white-space:nowrap}
.checks li{height:43px;display:flex;align-items:center;gap:22px}

/* testimonial */
.quote-band{position:absolute;left:0;top:1196px;width:1200px;height:176px;background:radial-gradient(ellipse at center,#fff 60%,#f4f4f3 100%)}
.quote{position:absolute;left:155px;top:1226px;width:900px;font-style:italic;font-size:17.5px;line-height:29px;color:#6a6a68}
.quote-rule{position:absolute;left:88px;top:1373px;width:1024px;height:2px;background:var(--line)}
.quote-rule::after{content:"";position:absolute;left:502px;top:-9px;width:16px;height:16px;background:#fff;
  border-left:2px solid var(--line);border-top:2px solid var(--line);transform:rotate(45deg)}
.quote-author{position:absolute;left:0;top:1392px;width:1200px;text-align:center;font-size:15px;color:#444}
.quote-author b{color:var(--green-dark)}
.quote-author small{font-size:13px}
.author-rule{position:absolute;left:88px;top:1428px;width:1024px;height:1px;background:var(--line)}
.partners{position:absolute;left:140px;top:1470px;width:925px;display:flex;justify-content:space-between;align-items:center}
.partners i{display:block;width:60px;height:36px;border-radius:18px;background:#cfcfcd}
.partners i:nth-child(3),.partners i:nth-child(4),.partners i:nth-child(5){width:78px;border-radius:4px}
.partners i:nth-child(6){width:48px;height:42px;border-radius:50%;background:#9d9d9b}

/* green box */
.service-box{position:absolute;left:90px;top:1559px;width:1020px;height:320px;border:4px solid #c5dd8a;
  background:linear-gradient(180deg,#c3db7f 0%,#9fc24f 45%,#85ad30 100%)}
.service-icon{position:absolute;left:18px;top:18px;width:50px;height:68px;border-radius:4px;background:linear-gradient(90deg,#111,#444)}
.service-box h2{position:absolute;left:80px;top:22px;font-weight:400;font-size:24px;color:#222}
.service-box hr{position:absolute;left:80px;top:64px;width:855px;border:none;border-top:1px solid rgba(255,255,255,.55)}
.perk{position:absolute;width:440px}
.perk .num{position:absolute;left:0;top:0;width:33px;height:33px;border-radius:50%;background:#fff;color:var(--green-dark);
  font-family:"Oswald",sans-serif;font-weight:600;font-size:20px;display:flex;align-items:center;justify-content:center}
.perk h4{margin-left:44px;font-family:"Oswald",sans-serif;font-weight:600;font-size:25px;line-height:33px;color:#fff;text-transform:uppercase;white-space:nowrap}
.perk p{margin:8px 0 0 44px;font-size:13px;line-height:19px;color:#f3f8e6;width:300px}

/* footer info */
.footer-info{position:absolute;left:0;top:1907px;width:1200px;height:338px;background:var(--soft)}
.col{position:absolute;top:1940px}
.col h5{font-weight:400;font-size:25px;color:#333;padding-bottom:12px;border-bottom:1px solid #d0d0ce;white-space:nowrap}
.col p{font-size:12.5px;line-height:19px;color:#555}
.col .lead{color:var(--green-dark);margin:20px 0 10px}
.col ul{list-style:none;font-size:12.5px;line-height:33px;color:#333;white-space:nowrap}
.services-lists{display:grid;grid-template-columns:209px 209px;margin-top:12px}
.col ul.links li{text-decoration:underline}
.col ul.contact{color:var(--green-dark);margin-top:12px}
.col-rule{position:absolute;top:1945px;width:1px;height:265px;background:#d0d0ce}
.btn-dark{position:absolute;top:2178px;width:108px;height:32px;background:#444442;border:1px solid #222;color:#fff;
  font-size:15px;display:flex;align-items:center;justify-content:center}

/* footer */
.site-footer{position:absolute;left:0;top:2245px;width:1200px;height:90px;background:#3a3a38;color:#ddd;font-size:13px}
.site-footer nav{position:absolute;left:88px;top:22px;white-space:nowrap}
.site-footer nav a{text-decoration:none;margin-right:11px}
.site-footer nav em{font-style:normal;margin-right:11px;color:#888}
.site-footer .copy{position:absolute;left:88px;top:54px;font-size:12.5px;color:#ccc}
.foot-social{position:absolute;left:1020px;top:22px;display:flex;gap:14px;font-size:14px;font-weight:700;color:#fff;align-items:center;white-space:nowrap}
.foot-social i{display:inline-block;width:14px;height:14px;border-radius:50%;background:#fff;margin-right:5px;vertical-align:-2px}
</style>
</head>
<body>

<header class="site-header">
  <div class="top-tab">
    <span><svg width="22" height="22" viewBox="0 0 22 22"><circle cx="11" cy="11" r="10" fill="#2f5fb3"/><text x="11" y="16" text-anchor="middle" fill="#fff" font-size="15" font-family="Arimo,sans-serif" font-weight="700">?</text></svg>Questions?</span>
    <span><svg width="20" height="20" viewBox="0 0 24 24"><path d="M6.6 10.8a15 15 0 0 0 6.6 6.6l2.2-2.2c.3-.3.7-.4 1-.2 1.1.4 2.3.6 3.6.6.6 0 1 .4 1 1V20c0 .6-.4 1-1 1A17 17 0 0 1 3 4c0-.6.4-1 1-1h3.5c.6 0 1 .4 1 1 0 1.3.2 2.5.6 3.6.1.3 0 .7-.2 1z" fill="#2f5fb3"/></svg>Call now! 0.800.000.zorpax</span>
  </div>

  <div class="brand"><span class="brand-square"></span>Zorpax</div>

  <div class="account-links">
    <div class="account-link"><span class="ico" role="img" aria-label="User icon"></span><div><b>User Registration</b><small>Click here</small></div></div>
    <div class="account-link"><span class="ico" role="img" aria-label="Customer icon"></span><div><b>Customer Login</b><small>Click here</small></div></div>
    <div class="account-link"><span class="ico" role="img" aria-label="Chat bubbles icon"></span><div><b>Live Chat Online</b><small>Click here</small></div></div>
  </div>

  <nav class="main-nav">
    <a class="active" style="width:119px">HOME</a>
    <a style="width:126px">ABOUT US</a>
    <a style="width:138px">DOMAINS</a>
    <a style="width:156px">WEB HOSTING</a>
    <a style="width:149px">MY ACCOUNT</a>
    <a style="width:147px">CONTACT US</a>
    <a style="width:177px">TESTIMONIALS</a>
  </nav>

  <section class="hero">
    <div class="server-rack" role="img" aria-label="Row of three dedicated server racks"></div>
    <h1 class="hero-title">Dedicated Servers</h1>
    <ul class="hero-list">
      <li><svg width="14" height="12" viewBox="0 0 14 12"><path d="M0 6h10M6 1l5 5-5 5" stroke="#9cc547" stroke-width="2.4" fill="none"/></svg>Nunc ut ante vel dolor volutpat</li>
      <li><svg width="14" height="12" viewBox="0 0 14 12"><path d="M0 6h10M6 1l5 5-5 5" stroke="#9cc547" stroke-width="2.4" fill="none"/></svg>Sed ac elit nec tellus aliquam</li>
      <li><svg width="14" height="12" viewBox="0 0 14 12"><path d="M0 6h10M6 1l5 5-5 5" stroke="#9cc547" stroke-width="2.4" fill="none"/></svg>Etiam elementum ornare dui</li>
      <li><svg width="14" height="12" viewBox="0 0 14 12"><path d="M0 6h10M6 1l5 5-5 5" stroke="#9cc547" stroke-width="2.4" fill="none"/></svg>Phasellus pellentesque vestibulum</li>
    </ul>
    <div class="price-box">
      <span class="price-only">only @</span>
      <span class="price-link">Login and get offers</span>
      <span class="price-value">$00.00</span>
    </div>
    <div class="price-lock" role="img" aria-label="Padlock with user figure"></div>
    <div class="dots"><i></i><i></i><i></i><i></i></div>
  </section>
</header>

<div class="social-links"><span><i></i>Chirpr</span><span><i></i>Facefeed</span></div>

<div class="info-strip">
  <p>Nunc aliquet eros vitae urna interdum vitae ullamcorper risus consectetur&nbsp; sit amet ultricies nunc sollicitudin. <a>View more</a></p>
  <div class="connect">Connect with us :</div>
</div>

<article class="plan" style="left:90px">
  <h3>DEDICATED SEVERS</h3>
  <span class="cost">$39</span>
  <ul><li>Mauris purus eget</li><li>Cras vel sem eget</li><li>Proin sed eros vitae</li><li>Pellentesque</li></ul>
  <div class="art" role="img" aria-label="Office building" style="background:linear-gradient(160deg,#e8eef6,#8fa9c9 60%,#dfe6ee)"></div>
  <span class="btn-green">SINGUP NOW</span>
</article>
<article class="plan" style="left:442px">
  <h3>WEB HOSTING</h3>
  <span class="cost">$219</span>
  <ul><li>Mauris purus eget</li><li>Cras vel sem eget</li><li>Proin sed eros vitae</li><li>Pellentesque</li></ul>
  <div class="art" role="img" aria-label="Blue globe with network ring" style="background:radial-gradient(circle at 50% 50%,#5aa0e6,#1c5aa8 55%,#eceff2 75%)"></div>
  <span class="btn-green">SINGUP NOW</span>
</article>
<article class="plan" style="left:792px">
  <h3>VIRTUAL SEVERS</h3>
  <span class="cost">$395</span>
  <ul><li>Mauris purus eget</li><li>Cras vel sem eget</li><li>Proin sed eros vitae</li><li>Pellentesque</li></ul>
  <div class="art" role="img" aria-label="Figure carrying a globe" style="background:radial-gradient(circle at 50% 40%,#4d8ed6,#2a63ab 40%,#e6e6e6 70%)"></div>
  <span class="btn-green">SINGUP NOW</span>
</article>

<div class="support-photo" role="img" aria-label="Support agent giving thumbs up beside server units"></div>
<p class="features-intro">At vero eos et accusamus et iusto odio dignissimos ducimus qui blanditiis praesentium voluptatum deleniti atque corrupti quos dolores et quas molestias excepturi sint occaecati cupiditate non provident, similique sunt in culpa qui officia deserunt mollitia animi, id est laborum et dolorum fuga.</p>
<ul class="checks" style="left:422px">
  <li><svg width="22" height="18" viewBox="0 0 22 18"><path d="M2 9l6 6L20 2" stroke="#7fb52c" stroke-width="4" fill="none"/></svg>100% Network Uptime SLA</li>
  <li><svg width="22" height="18" viewBox="0 0 22 18"><path d="M2 9l6 6L20 2" stroke="#7fb52c" stroke-width="4" fill="none"/></svg>ISO 9001:2008 Certified</li>
  <li><svg width="22" height="18" viewBox="0 0 22 18"><path d="M2 9l6 6L20 2" stroke="#7fb52c" stroke-width="4" fill="none"/></svg>24/7 ITIL Technical Support</li>
</ul>
<ul class="checks" style="left:794px">
  <li><svg width="22" height="18" viewBox="0 0 22 18"><path d="M2 9l6 6L20 2" stroke="#7fb52c" stroke-width="4" fill="none"/></svg>Sed ac elit nec tellus aliquam</li>
  <li><svg width="22" height="18" viewBox="0 0 22 18"><path d="M2 9l6 6L20 2" stroke="#7fb52c" stroke-width="4" fill="none"/></svg>Praesent vehicula augue</li>
  <li><svg width="22" height="18" viewBox="0 0 22 18"><path d="M2 9l6 6L20 2" stroke="#7fb52c" stroke-width="4" fill="none"/></svg>Nunc aliquet eros vitae urna</li>
</ul>

<div class="quote-band"></div>
<blockquote class="quote">“ On the other hand, we denounce with righteous indignation and dislike men who are so beguiled and demoralized by the charms of pleasure of the moment, so blinded by desire, that they cannot foresee the pain and trouble that are bound to ensue; and equal blame belongs to those who fail in their duty through weakness of will, which is the same as saying through shrinking from toil and pain. ”</blockquote>
<div class="quote-rule"></div>
<p class="quote-author"><b>Martin Hale</b> - <small>Anterdum vitae</small></p>
<div class="author-rule"></div>
<div class="partners"><i></i><i></i><i></i><i></i><i></i><i></i><i></i><i></i><i></i></div>

<section class="service-box">
  <div class="service-icon" role="img" aria-label="Server tower"></div>
  <h2>DEDICATED SERVERS</h2>
  <hr>
  <div class="perk" style="left:96px;top:107px"><span class="num">1</span><h4>Business Class Hardware</h4><p>Atvero eoset accusamus etiusto odio dignis simos ducimus qui blanditiis.</p></div>
  <div class="perk" style="left:533px;top:107px"><span class="num">2</span><h4>24/7/365 Expert Technical Support</h4><p>Atvero eoset accusamus etiusto odio dignis simos ducimus qui blanditiis.</p></div>
  <div class="perk" style="left:96px;top:217px"><span class="num">3</span><h4>Fast Setup</h4><p>Atvero eoset accusamus etiusto odio dignis simos ducimus qui blanditiis.</p></div>
  <div class="perk" style="left:533px;top:217px"><span class="num">4</span><h4>Dedicated Account Manager</h4><p>Atvero eoset accusamus etiusto odio dignis simos ducimus qui blanditiis.</p></div>
</section>

<section class="footer-info"></section>
<div class="col" style="left:108px;width:305px">
  <h5>ABOUT ZORPAX</h5>
  <p class="lead">At vero eos et accusamus et iusto odio dignissimos ducimus qui blanditiis praesentium voluptatum.</p>
  <p>Neque porro quisquam est, qui dolorem ipsum quia dolor sit amet, consectetur, adipisci velit, sed quia non numquam eius modi tempora incidunt ut labore et dolore magnam aliquam quaerat voluptatem. Ut enim ad minima veniam.</p>
</div>
<div class="col-rule" style="left:442px"></div>
<div class="col" style="left:470px;width:378px">
  <h5>SERVICES</h5>
  <div class="services-lists">
    <ul class="links"><li>100% Network Uptime SLA</li><li>ISO 9001:2008 Certified</li><li>24/7 ITIL Technical Support</li><li>Etiam elementum ornare</li><li>Phasellus pellentesque</li></ul>
    <ul class="links"><li>100% Network Uptime SLA</li><li>ISO 9001:2008 Certified</li><li>24/7 ITIL Technical Support</li><li>Etiam elementum ornare</li><li>Phasellus pellentesque</li></ul>
  </div>
</div>
<div class="col-rule" style="left:875px"></div>
<div class="col" style="left:903px;width:207px">
  <h5>CONTACT US</h5>
  <ul class="contact"><li>Call us : 0.800.000zorpax</li><li>Toll free Number : 0.800.000zorpax</li><li>Fax : 0.800.000zorpax</li><li>E -mail : info@zorpaxsupport.com</li><li>Live Chat Online</li></ul>
</div>
<span class="btn-dark" style="left:108px">VIEW MORE</span>
<span class="btn-dark" style="left:470px">VIEW MORE</span>
<span class="btn-dark" style="left:903px">VIEW MORE</span>

<footer class="site-footer">
  <nav><a>Home</a><em>|</em><a>About us</a><em>|</em><a>Domains</a><em>|</em><a>Web hosting</a><em>|</em><a>My Account</a><em>|</em><a>Contact us</a><em>|</em><a>Testimonials</a><em>|</em><a>Terms and conditions</a><em>|</em><a>Privacy policy</a></nav>
  <p class="copy">Copyright © 2012 www.zorpaxservers.com&nbsp;&nbsp; All rights reserved.</p>
  <div class="foot-social"><span><i></i>Facefeed</span><span><i></i>Chirpr</span></div>
</footer>

</body>
</html>
```